Cardiology practice business card

We need a business card for our cardiology practice "Wattle Cardiology". We have a new logo, attached below. We like the colours in the logo - red and charcoal. The front of the business card will need to have the doctors name, address, phone number and email. The back will need to have space to write 2 appointment dates and times.

```html
<!DOCTYPE html>
<html lang="en">
<head>
<meta charset="utf-8">
<title>Wattle Cardiology – Business Card</title>
<link rel="stylesheet" href="https://fonts.googleapis.com/css2?family=Montserrat:wght@500;600;700&family=Lato:wght@400;700&display=swap">
<style>
  :root {
    --backdrop: #c6c6c6;
    --card: #ffffff;
    --red: #d3151c;
    --red-dark: #7e0006;
    --red-mid: #b30810;
    --charcoal: #3a3a3c;
    --ink: #222222;
    --rule: #2b2b2b;
  }
  * { margin: 0; padding: 0; box-sizing: border-box; }
  html, body { width: 785px; height: 1200px; overflow: hidden; }
  body {
    background: var(--backdrop);
    font-family: "Lato", Arial, sans-serif;
    color: var(--ink);
    position: relative;
  }
  .card {
    position: absolute;
    left: 169px;
    width: 447px;
    height: 255px;
    background: var(--card);
    border-radius: 11px;
    overflow: hidden;
    box-shadow: 0 3px 5px rgba(0,0,0,0.25);
  }
  .card--front { top: 124px; }
  .card--back-one { top: 447px; }
  .card--back-two { top: 775px; }

  .card-label {
    position: absolute;
    left: 169px;
    width: 447px;
    text-align: center;
    font-family: "Montserrat", Arial, sans-serif;
    font-weight: 500;
    font-size: 17px;
    letter-spacing: 5px;
    color: #222;
  }
  .card-label--front { top: 401px; }
  .card-label--back-one { top: 725px; }
  .card-label--back-two { top: 1059px; }

  /* Front */
  .brand-name {
    font-family: "Montserrat", Arial, sans-serif;
    font-weight: 600;
    color: var(--red);
    letter-spacing: 2px;
    line-height: 1;
  }
  .front-brand {
    position: absolute;
    top: 38px;
    left: 0;
    width: 100%;
    display: flex;
    align-items: center;
    justify-content: center;
    gap: 10px;
  }
  .front-brand .mark-dot {
    width: 14px; height: 14px; border-radius: 50%;
    background: var(--red);
  }
  .front-brand .brand-name {
    font-size: 22px;
    text-align: left;
  }
  .front-brand .brand-name span { display: block; }
  .front-brand .brand-name .line-two { font-size: 17px; margin-top: 5px; letter-spacing: 3px; }

  .front-rule {
    position: absolute;
    left: 0; top: 138px;
    width: 100%; height: 1.5px;
    background: linear-gradient(90deg, var(--rule) 0%, var(--rule) 50%, rgba(43,43,43,0) 100%);
  }
  .front-band {
    position: absolute;
    left: 0; top: 142px;
    width: 100%; height: 113px;
    background: radial-gradient(ellipse 70% 120% at 45% 80%, #e01219 0%, var(--red-mid) 45%, var(--red-dark) 100%);
    color: #fff;
  }
  .person {
    position: absolute;
    right: 249px;
    top: 34px;
    text-align: right;
  }
  .person-name {
    font-family: "Montserrat", Arial, sans-serif;
    font-weight: 700;
    font-size: 19.5px;
    letter-spacing: 0.3px;
    white-space: nowrap;
  }
  .person-role { font-size: 11.5px; margin-top: 3px; }
  .band-divider {
    position: absolute;
    left: 220px; top: 22px;
    width: 1px; height: 64px;
    background: rgba(255,255,255,0.85);
  }
  .contact {
    position: absolute;
    left: 239px; top: 20px;
    list-style: none;
    font-size: 10.8px;
    line-height: 16px;
  }
  .contact li { display: flex; align-items: flex-start; }
  .contact svg { width: 9px; height: 9px; margin-top: 3.5px; margin-right: 10px; flex: none; fill: #fff; }
  .contact .gap { margin-top: 2px; }

  /* Back */
  .back-brand { position: absolute; top: 29px; }
  .back-brand .brand-name span { display: block; }
  .back-brand .line-one { font-size: 36px; letter-spacing: 2.5px; }
  .back-brand .line-two { font-size: 20px; letter-spacing: 3.5px; margin-top: 6px; }
  .card--back-one .back-brand { left: 39px; text-align: left; }
  .card--back-two .back-brand { left: 0; width: 100%; text-align: center; top: 27px; }

  .referral {
    position: absolute;
    top: 110px;
    font-size: 12px;
    display: flex;
    align-items: baseline;
    gap: 10px;
  }
  .referral-title {
    font-family: "Montserrat", Arial, sans-serif;
    font-weight: 600;
    font-size: 15.5px;
    letter-spacing: 2.5px;
    color: var(--red);
  }
  .card--back-one .referral { left: 39px; }
  .card--back-two .referral { left: 0; width: 100%; justify-content: center; padding-left: 28px; }

  .appointment {
    position: absolute;
    left: 39px;
    width: 367px;
    display: flex;
    align-items: flex-end;
    font-size: 11px;
    line-height: 1;
  }
  .appointment--first { top: 150px; }
  .appointment--second { top: 187px; }
  .appointment .fill { border-bottom: 1px solid var(--rule); height: 1px; margin-bottom: 0.5px; }
  .appointment .fill--date { width: 164px; }
  .appointment .fill--time { flex: 1; }

  .notice {
    position: absolute;
    left: 0; top: 222px;
    width: 100%;
    text-align: center;
    font-size: 6.4px;
    line-height: 8.3px;
    color: #333;
  }
</style>
</head>
<body>

  <section class="card card--front" aria-label="Front of card">
    <div class="front-brand">
      <div class="mark-dot"></div>
      <div class="brand-name"><span class="line-one">WATTLE</span><span class="line-two">CARDIOLOGY</span></div>
    </div>
    <div class="front-rule"></div>
    <div class="front-band">
      <div class="person">
        <div class="person-name">DANIEL HARTLEY</div>
        <div class="person-role">Cardiologist &amp; CEO</div>
      </div>
      <div class="band-divider"></div>
      <ul class="contact">
        <li>
          <svg viewBox="0 0 10 10" aria-hidden="true"><path d="M5 0C3 0 1.6 1.5 1.6 3.4 1.6 5.8 5 10 5 10s3.4-4.2 3.4-6.6C8.4 1.5 7 0 5 0zm0 4.8a1.4 1.4 0 1 1 0-2.8 1.4 1.4 0 0 1 0 2.8z"/></svg>
          <span>423 Street Address Here, City<br>State &amp; Country, ZIP Code</span>
        </li>
        <li class="gap">
          <svg viewBox="0 0 10 10" aria-hidden="true"><path d="M2 .5l1.6 2.2-.9 1.1c.6 1.3 1.6 2.3 2.9 2.9l1.1-.9L9 7.4 8.2 9C4.2 8.9 1 5.7.9 1.6z"/></svg>
          <span>(123) 456-7890</span>
        </li>
        <li class="gap">
          <svg viewBox="0 0 10 10" aria-hidden="true"><path d="M.5 2h9v6.5h-9zM1 2.4l4 3 4-3v1L5 6.4 1 3.4z" fill-rule="evenodd"/></svg>
          <span>info@yourwebsitehere.com</span>
        </li>
      </ul>
    </div>
  </section>
  <div class="card-label card-label--front">FRONT CARD</div>

  <section class="card card--back-one" aria-label="Back of card, version one">
    <div class="back-brand">
      <div class="brand-name"><span class="line-one">WATTLE</span><span class="line-two">CARDIOLOGY</span></div>
    </div>
    <div class="referral"><span class="referral-title">NEW REFERRAL</span><span>YES &nbsp;/&nbsp; NO</span></div>
    <div class="appointment appointment--first"><span>DATE</span><span class="fill fill--date"></span><span>TIME</span><span class="fill fill--time"></span></div>
    <div class="appointment appointment--second"><span>DATE</span><span class="fill fill--date"></span><span>TIME</span><span class="fill fill--time"></span></div>
    <p class="notice">If you are unable to keep your appointment, please call us to<br>reschedule at least 48 hours prior to your appointment.</p>
  </section>
  <div class="card-label card-label--back-one">BACK CARD 01</div>

  <section class="card card--back-two" aria-label="Back of card, version two">
    <div class="back-brand">
      <div class="brand-name"><span class="line-one">WATTLE</span><span class="line-two">CARDIOLOGY</span></div>
    </div>
    <div class="referral"><span class="referral-title">NEW REFERRAL</span><span>YES &nbsp;/&nbsp; NO</span></div>
    <div class="appointment appointment--first"><span>DATE</span><span class="fill fill--date"></span><span>TIME</span><span class="fill fill--time"></span></div>
    <div class="appointment appointment--second"><span>DATE</span><span class="fill fill--date"></span><span>TIME</span><span class="fill fill--time"></span></div>
    <p class="notice">If you are unable to keep your appointment, please call us to<br>reschedule at least 48 hours prior to your appointment.</p>
  </section>
  <div class="card-label card-label--back-two">BACK CARD 02</div>

</body>
</html>
```